Venture Keystone - Client Appreciation Party Invitation and Poster

We need a printable invitation, a version of the same invitation that can be emailed out, and also a Poster of the invitation for our annual client appreciation party.

The location is called: The Lanternhouse. Here is a link to the location: https://www.thelanternhousevenue.example/

We like their font and their little logo that you see when you log onto this page. But we'd love to see creatively what you can come up with.

This party is for our clients who are interior designers and owners in the Hospitality industry. Here are the details which need to be included in the invitation:

Location: The Lanternhouse - 482 W Brindle Ave. Chicago IL 60614
Date/Time: Thursday August 23rd - 5:30-9:00pm
RSVP: Please RSVP to: gathering@venturekeystone.example

Then our Sponsors Logos need to be included on the bottom: I have uploaded those logos here as well as our Logo and a copy of the invitation we did for last year's party so you can see sort of what we've done in the past.

For the poster - we typically do a version of the invitation (see uploaded example of last year's poster) with the sponsor logos and the overall theme of the invitation just a bit simplified by removing the date/time/location info. We need this in a printable format which can be blown up to a 24x30 poster size.

Requirements
Must have
• use 2 to 3 colors only.
• logos of sponsors can be of the same color.

```html
<!DOCTYPE html>
<html lang="en">
<head>
<meta charset="utf-8">
<title>Venture Keystone – Weekend Warm Up</title>
<link rel="stylesheet" href="https://fonts.googleapis.com/css2?family=Lato:wght@400;700;900&family=Michroma&display=swap">
<style>
  :root {
    --red: #bd1e2d;
    --amber: #f5a93a;
    --orange: #f7a23a;
    --flame: #ee2a24;
    --black: #000000;
    --white: #ffffff;
    --ink: #333333;
  }
  * { margin: 0; padding: 0; box-sizing: border-box; }
  html, body { width: 1001px; height: 1200px; overflow: hidden; }
  body { background: var(--red); font-family: "Lato", sans-serif; }
  .invitation { position: relative; width: 1001px; height: 1200px; background: var(--red); }
  .frame {
    position: absolute; left: 29px; top: 35px; width: 943px; height: 1131px;
    border: 3px solid var(--white);
  }
  .host {
    position: absolute; top: 60px; left: 0; width: 100%;
    text-align: center; color: var(--white); font-weight: 700; font-size: 40px;
  }
  .title {
    position: absolute; top: 128px; left: 0; width: 100%;
    text-align: center; color: var(--amber);
    font-family: "Michroma", sans-serif; font-size: 60px; letter-spacing: 2px;
  }
  .emblem { position: absolute; left: 233px; top: 231px; width: 536px; height: 536px; }
  .tagline {
    position: absolute; top: 788px; left: 0; width: 100%;
    text-align: center; color: var(--white); font-weight: 700; font-size: 55px;
  }
  .date-block {
    position: absolute; left: 206px; top: 871px; width: 590px; height: 107px;
    background: linear-gradient(to bottom, var(--orange), var(--flame));
    color: var(--white); font-weight: 700; font-size: 36px; line-height: 45px;
    text-align: center; padding-top: 9px;
  }
  .detail {
    position: absolute; top: 991px; width: 390px; height: 86px;
    background: var(--black); color: var(--white);
    font-weight: 700; font-size: 22px; line-height: 28px;
    padding: 14px 16px;
  }
  .detail--location { left: 60px; }
  .detail--rsvp { left: 549px; padding-left: 14px; }
  .sponsors {
    position: absolute; left: 29px; top: 1084px; width: 943px; height: 82px;
    background: var(--white);
    display: flex; align-items: center; justify-content: space-around;
    padding: 0 20px;
  }
  .sponsor {
    display: flex; align-items: center; gap: 8px;
    color: var(--ink); font-size: 21px; font-weight: 400;
  }
  .sponsor-mark { width: 22px; height: 22px; background: var(--ink); }
  .sponsor-mark--round { border-radius: 50%; }
</style>
</head>
<body>
  <main class="invitation">
    <div class="frame"></div>
    <p class="host">Venture Keystone</p>
    <h1 class="title">WEEKEND WARM UP</h1>
    <svg class="emblem" viewBox="0 0 536 536" role="img" aria-label="Lion dance mask illustration in amber, red and pink on a black circle">
      <circle cx="268" cy="268" r="268" fill="var(--black)"/>
      <circle cx="268" cy="260" r="180" fill="#c7772f" opacity="0.55"/>
    </svg>
    <p class="tagline">client appreciation event</p>
    <div class="date-block">THURSDAY AUGUST 23RD<br>5:30-9:00PM</div>
    <div class="detail detail--location">Location: The Lanternhouse - 482 W Brindle Ave. Chicago IL 60614</div>
    <div class="detail detail--rsvp">RSVP: Please RSVP to: gathering@venturekeystone.example</div>
    <footer class="sponsors">
      <span class="sponsor"><span class="sponsor-mark"></span>Brightfield</span>
      <span class="sponsor"><span class="sponsor-mark"></span>Dalewood</span>
      <span class="sponsor">Arbor</span>
      <span class="sponsor"><span class="sponsor-mark sponsor-mark--round"></span>Lumeno</span>
      <span class="sponsor">Halcrest</span>
      <span class="sponsor">Ridgeway Hospitality</span>
    </footer>
  </main>
</body>
</html>
```